Business card design for strategy and management consulting company. Would like to have a clean and professional business card, based on the attached logo. The company is a strategy and management consulting company focusing on sustainable business modlels based on economic, social and environmental market opportunities. Preferably the logo should be included on both sides of the design.

Industry/Entity Type

Business

Contact Information for Business Card

Halvor Brekkeli, CEO/Management consultant
halvor.brekkeli@morvikpartners.example
Mob: +47 936 28 417
Office: Lyngvedens gate 14, pb 312 sentrum, N-0158 Oslo Norway

Requirements
Must have
• Include attached logo
Nice to have
• Would like to have the logo on both sides
Should not have
• Many colours.

```html
<!DOCTYPE html>
<html lang="en">
<head>
<meta charset="utf-8">
<title>Morvik business card</title>
<link rel="stylesheet" href="https://fonts.googleapis.com/css2?family=Open+Sans:wght@400;600;700&display=swap">
<style>
  :root {
    --backdrop: #1d1d1f;
    --card-white: #fbfbfb;
    --ink: #262626;
    --band: #3f3f41;
    --accent: #f2cf1f;
    --sky-top: #dde7ef;
    --sky-bottom: #eef2f4;
    --muted: #6b6b6b;
  }
  * { box-sizing: border-box; margin: 0; padding: 0; }
  html, body { width: 1200px; height: 900px; overflow: hidden; }
  body {
    background: var(--backdrop);
    font-family: "Open Sans", Arial, sans-serif;
    position: relative;
  }
  .card {
    position: absolute;
    left: 290px;
    width: 620px;
    height: 354px;
    overflow: hidden;
    box-shadow: 0 10px 30px rgba(0,0,0,.5);
  }
  .card--front { top: 76px; background: var(--card-white); }
  .card--back { top: 470px; background: var(--sky-bottom); }

  .wordmark {
    display: flex;
    align-items: center;
    gap: 10px;
    font-weight: 700;
    letter-spacing: -1px;
    line-height: 1;
  }
  .wordmark__dot {
    width: 14px; height: 14px;
    border-radius: 50%;
    background: var(--accent);
  }
  .card--front .wordmark {
    position: absolute;
    left: 50%; top: 50%;
    transform: translate(-50%, -50%);
    font-size: 78px;
    color: var(--ink);
  }

  .back__band {
    position: absolute; left: 0; top: 0;
    width: 100%; height: 150px;
    background: var(--band);
  }
  .card--back .wordmark {
    position: absolute;
    left: 50%; top: 72px;
    transform: translateX(-50%);
    font-size: 66px;
    color: #ffffff;
  }
  .back__sky {
    position: absolute; left: 0; top: 150px;
    width: 100%; height: 204px;
    background: linear-gradient(180deg, var(--sky-top) 0%, var(--sky-bottom) 70%, #e3e8ec 100%);
  }
  .contact {
    position: absolute;
    left: 0; top: 158px;
    width: 100%;
    text-align: center;
    color: var(--ink);
  }
  .contact__name { font-size: 27px; font-weight: 600; }
  .contact__role { font-size: 12px; color: var(--muted); margin-bottom: 30px; }
  .contact__line { font-size: 14px; line-height: 1.45; }
</style>
</head>
<body>
  <section class="card card--front" aria-label="Card front">
    <div class="wordmark"><span>Morvik</span><span class="wordmark__dot"></span></div>
  </section>

  <section class="card card--back" aria-label="Card back">
    <div class="back__band"></div>
    <div class="back__sky" role="img" aria-label="Pale photo of a hazy sky over distant mountains with a hot air balloon"></div>
    <div class="wordmark"><span>Morvik</span><span class="wordmark__dot"></span></div>
    <div class="contact">
      <p class="contact__name">Halvor Brekkeli</p>
      <p class="contact__role">CEO/Management consultant</p>
      <p class="contact__line">+47 936 28 417</p>
      <p class="contact__line">halvor.brekkeli@morvikpartners.example</p>
      <p class="contact__line">Lyngvedens gate 14, pb 312 sentrum, Oslo Norway</p>
    </div>
  </section>
</body>
</html>
```